business card for a massage therapy practice named 'Meadow and Willow Massage Studio'

I really need a trendy, yet easy on the eyes business card to complement my logo. Ideally with some gold or rose gold foil work.

My uploaded file of the logo I have in horizontal but I have a vertical version as well. Another color that is used in the website is a blush pink here and there. I'd like to see some trendy tropical leaves in the design.

```html
<!DOCTYPE html>
<html lang="en">
<head>
<meta charset="utf-8">
<title>Meadow and Willow Massage Studio – Business Card</title>
<link rel="stylesheet" href="https://fonts.googleapis.com/css2?family=Jost:wght@400;500;600&display=swap">
<style>
  :root {
    --card-pink: #fe45e5;
    --foil-gold: #e9b63a;
    --mark-olive: #a39547;
    --ink-dark: #1b1418;
    --text-white: #ffffff;
  }
  html, body {
    margin: 0;
    padding: 0;
    width: 1200px;
    height: 686px;
    overflow: hidden;
    background: var(--foil-gold);
  }
  .card {
    position: relative;
    box-sizing: border-box;
    width: 1200px;
    height: 686px;
    border: 8px solid var(--foil-gold);
    background: var(--card-pink);
    font-family: "Jost", "Futura", sans-serif;
  }
  .brand {
    position: absolute;
    left: 256px;
    top: 110px;
    display: flex;
    align-items: center;
    gap: 34px;
  }
  .brand-mark {
    width: 96px;
    height: 96px;
    flex: none;
  }
  .brand-name {
    margin: 0;
    font-weight: 500;
    font-size: 52px;
    line-height: 1.15;
    color: var(--ink-dark);
    letter-spacing: 0.5px;
  }
  .contact {
    position: absolute;
    left: 0;
    right: 0;
    top: 390px;
    text-align: center;
    color: var(--text-white);
  }
  .contact-name {
    margin: 0 0 14px;
    font-weight: 600;
    font-size: 36px;
    letter-spacing: 3.5px;
    text-transform: uppercase;
  }
  .contact-line {
    margin: 0;
    font-weight: 400;
    font-size: 31px;
    line-height: 57px;
    letter-spacing: 1px;
  }
  .contact-web {
    letter-spacing: 2.5px;
  }
</style>
</head>
<body>
  <main class="card">
    <header class="brand">
      <svg class="brand-mark" viewBox="0 0 96 96" aria-hidden="true">
        <circle cx="48" cy="48" r="46" fill="var(--mark-olive)"/>
      </svg>
      <h1 class="brand-name">Meadow and Willow<br>Massage Studio</h1>
    </header>
    <section class="contact">
      <p class="contact-name">Daniela Reyes LMT</p>
      <p class="contact-line">916.555.0148</p>
      <p class="contact-line">meadowandwillow@mail.com</p>
      <p class="contact-line contact-web">www.meadowandwillow.com</p>
    </section>
  </main>
</body>
</html>
```